Packaging design for aloe lotion bottle for a Laser Clinic

We need a packaging design for a body lotion bottle. Our business is a laser clinic and we are looking at slowly rolling out a range of skincare products. This lotion bottle is the first item with more to follow so the winning designer will have other designs to work on in the future.

The design needs to be classy, elegant, strong and sophisticated. The bottle will be clear with a shiny silver sleeved lid. The lotion itself, which will be visible through the bottle, will be a very light green colour. Think Mirelle Vantrau and Doriva as that is the image I want to convey.

Ideally we were thinking of having a design with a single colour but if you come up with a fantastic multi colour design that we love then we're open to it.

Reason: I have extended the deadline as I feel I need more time to allow designers to submit their designs. I haven't found a design that I love just yet. The project has been made a guaranteed payment upon completion. Thank you.

Target Market(s)

upper class high income earners with a high disposable income. People that look after themselves

Industry/Entity Type

Beauty Salon

Colors
000000
cadf82

Requirements
Must have
• must include the details below:
• After Beam Soothing Balm
• This soothing and calming anti inflammatory cream is specifically formulated for use after post laser treatments.
• Fresh Cucumber, Melon and Aloe Vera Leaf Juice blend together in perfect harmony to quickly cool you skin and restore your skins natural moisture.
• Our luxurious calming cream targets redness and helps to reduce inflammation, bringing you supple and radiant skin like never before.
• Directions: Use a liberal amount twice daily on all your treatment areas. This nourishing cream can also be used daily to restore moisture and softness to areas of the face and body not being treated by laser or IPL.
• Ingredients: water (aqua), glycine soja (soybean) oil, cetyl alcohol, glycerin dimethicone, butyrospermum parkii (shea butter), theobroma cacao (cocoa) seed butter, aloe barbadensis (aloe vera) leaf juice, tocopheryl acetate, sodium ascorbyl phosphate, disodium EDTA, ceteareth-20, carbomer, BHT, benzyl benzoate, butylphenyl methylpropional, hexyl cinnamal, linalool, glyceryl caprylate, methylisothiazolinone. May contain: Red 4 (CI 14700, aka 504), Yellow 5 (CI 19140, Ki4), Yellow 6 (CI 15985, KI5), Blue 1 (CI 42090, Ao1), Red 33 (CI 17200, Aka 227), Ext. Violet 2 (CI 60730, Murasaki401), Green 3 (CI 42053, Midori3)
• Against Animal Testing
• Manufactured in Australia
• www.velvetbloomclinic.example.com.au
• 500ml
• Pure Glow Laser Hair Removal logo (see attached files)
Nice to have
• A sophisticated and elegant design
Should not have
• no photos. not too many different colours

```html
<!DOCTYPE html>
<html lang="en">
<head>
<meta charset="UTF-8">
<title>Aloe Lotion Label – Pure Glow Laser Hair Removal</title>
<link href="https://fonts.googleapis.com/css2?family=Libre+Baskerville:wght@400;700&family=Quicksand:wght@400;500&display=swap" rel="stylesheet">
<style>
  :root {
    --lotion-green: #dde7d3;
    --ink: #111111;
    --ink-soft: #2a2a2a;
    --gold-light: #f6dc8e;
    --gold: #e2b448;
  }
  * { margin: 0; padding: 0; box-sizing: border-box; }
  html, body {
    width: 1200px;
    height: 1200px;
    overflow: hidden;
    background: var(--lotion-green);
  }
  .label {
    position: relative;
    width: 1200px;
    height: 1200px;
    color: var(--ink);
    font-family: "Quicksand", sans-serif;
  }
  .label__column {
    position: absolute;
    left: 405px;
    top: 36px;
    width: 390px;
    height: 1140px;
    display: flex;
    flex-direction: column;
  }
  .product-title {
    font-family: "Libre Baskerville", serif;
    font-weight: 700;
    font-size: 58px;
    line-height: 74px;
    letter-spacing: 2px;
  }
  .gold-rule {
    margin-top: 8px;
    width: 390px;
    height: 4px;
    border-radius: 2px;
    background: linear-gradient(90deg, var(--gold), var(--gold-light) 50%, var(--gold));
  }
  .product-name {
    margin-top: 12px;
    font-family: "Libre Baskerville", serif;
    font-size: 15px;
    letter-spacing: 3px;
    text-transform: uppercase;
  }
  .intro {
    margin-top: 16px;
    width: 360px;
    font-size: 23px;
    line-height: 31px;
  }
  .benefit {
    margin-top: 14px;
    font-size: 15px;
    line-height: 21px;
    color: var(--ink-soft);
  }
  .ingredients-blurb {
    margin-top: 26px;
    width: 370px;
    font-size: 23px;
    line-height: 31px;
  }
  .ingredients-blurb .key {
    font-size: 28px;
    font-weight: 500;
  }
  .directions {
    margin-top: 18px;
    font-size: 12.5px;
    line-height: 17px;
    color: var(--ink-soft);
  }
  .ingredients-list {
    margin-top: 10px;
    font-size: 10px;
    line-height: 13px;
    color: var(--ink-soft);
  }
  .fine-label { font-weight: 500; color: var(--ink); }
  .maker {
    margin-top: 18px;
    width: 390px;
  }
  .maker__by {
    display: flex;
    align-items: flex-end;
    gap: 4px;
    font-size: 17px;
    font-weight: 500;
  }
  .maker__rule {
    flex: 1;
    height: 2px;
    margin-bottom: 3px;
    background: var(--ink);
  }
  .maker__name {
    margin-top: 8px;
    font-size: 26px;
    line-height: 32px;
    font-weight: 500;
    white-space: nowrap;
  }
  .claims {
    margin-top: 12px;
    display: flex;
    justify-content: space-between;
    font-size: 12px;
    letter-spacing: 1px;
    text-transform: uppercase;
  }
  .website {
    margin-top: 4px;
    font-size: 12px;
    letter-spacing: 0.5px;
  }
  .volume {
    margin-top: auto;
    text-align: center;
    font-size: 24px;
    font-weight: 500;
  }
</style>
</head>
<body>
  <main class="label">
    <div class="label__column">
      <h1 class="product-title">ALOE<br>LOTION</h1>
      <div class="gold-rule"></div>
      <p class="product-name">After Beam Soothing Balm</p>

      <p class="intro">This soothing and calming anti inflammatory cream is specifically formulated for use after post laser treatments.</p>

      <p class="benefit">Our luxurious calming cream targets redness and helps to reduce inflammation, bringing you supple and radiant skin like never before.</p>

      <p class="ingredients-blurb">Fresh <span class="key">Cucumber,</span> <span class="key">Melon</span> and <span class="key">Aloe Vera Leaf</span> Juice blend together in perfect harmony to quickly cool you skin and restore your skins natural moisture.</p>

      <p class="directions"><span class="fine-label">Directions:</span> Use a liberal amount twice daily on all your treatment areas. This nourishing cream can also be used daily to restore moisture and softness to areas of the face and body not being treated by laser or IPL.</p>

      <p class="ingredients-list"><span class="fine-label">Ingredients:</span> water (aqua), glycine soja (soybean) oil, cetyl alcohol, glycerin dimethicone, butyrospermum parkii (shea butter), theobroma cacao (cocoa) seed butter, aloe barbadensis (aloe vera) leaf juice, tocopheryl acetate, sodium ascorbyl phosphate, disodium EDTA, ceteareth-20, carbomer, BHT, benzyl benzoate, butylphenyl methylpropional, hexyl cinnamal, linalool, glyceryl caprylate, methylisothiazolinone. May contain: Red 4 (CI 14700, aka 504), Yellow 5 (CI 19140, Ki4), Yellow 6 (CI 15985, KI5), Blue 1 (CI 42090, Ao1), Red 33 (CI 17200, Aka 227), Ext. Violet 2 (CI 60730, Murasaki401), Green 3 (CI 42053, Midori3)</p>

      <div class="maker">
        <div class="maker__by"><span>BY</span><span class="maker__rule"></span></div>
        <p class="maker__name">Pure Glow Laser Hair Removal</p>
      </div>

      <div class="claims"><span>Against Animal Testing</span><span>Manufactured in Australia</span></div>
      <p class="website">www.velvetbloomclinic.example.com.au</p>

      <p class="volume">500ml</p>
    </div>
  </main>
</body>
</html>
```